Business Card Design Project - Sports Brand

Brisk is a e-commerce fitness wear brand for ladies who are into gym, pole and swim.

Card should not be overly cluttered and should include the following:

1. logo
2. Name of the company (Use "Brisk Loom Pte Ltd" for now)
3. Address of company (Use a mock address)
4. Representative's name and contact info etc. (use a mock name and contact info)
5. website address

Target Market(s)

Women who are into pole , gym, and swim.

Women who shop online

Industry/Entity Type

E-Commerce

Colors

Designer to choose colors to be used in the design.

Requirements
Nice to have
• feminine sublimation of colours

Need not be printed on traditional paper. We would like the design to be revolutionary and interesting to the eye :)
Should not have
• the design should not be traditional looking. Do not include illustrations of Bikinis, yoga poses etc. in the card.

```html
<!DOCTYPE html>
<html lang="en">
<head>
<meta charset="utf-8">
<title>Brisk Loom Pte Ltd – Business Card</title>
<link href="https://fonts.googleapis.com/css2?family=Questrial&family=Roboto:wght@700&display=swap" rel="stylesheet">
<style>
  :root {
    --backdrop: #262626;
    --card-white: #f4f4f4;
    --card-shade: #e6e6e6;
    --brand-red: #c8262f;
    --brand-red-light: #db3a42;
    --brand-red-dark: #a91d26;
    --accent-orange: #e2542a;
    --logo-pink: #e8508a;
    --logo-orange: #f07a3a;
    --ink-crimson: #b4182c;
    --ink-dark: #3a3a3a;
    --ink-white: #ffffff;
    --ink-soft: #f6d6d8;
  }
  * { box-sizing: border-box; margin: 0; padding: 0; }
  html, body { width: 1200px; height: 900px; overflow: hidden; }
  body {
    background: var(--backdrop);
    display: flex;
    flex-direction: column;
    align-items: center;
    justify-content: center;
    gap: 30px;
  }
  .card {
    position: relative;
    width: 720px;
    height: 411px;
    background: linear-gradient(135deg, var(--card-white), var(--card-shade));
    box-shadow: 0 10px 30px rgba(0,0,0,0.45);
    overflow: hidden;
  }
  .brand-lockup {
    position: absolute;
    display: flex;
    flex-direction: column;
    align-items: flex-start;
  }
  .brand-lockup .brand-row {
    display: flex;
    align-items: center;
    gap: 14px;
  }
  .brand-mark {
    width: 92px;
    height: 92px;
    border-radius: 50%;
    background: radial-gradient(circle at 40% 40%, var(--logo-orange), var(--logo-pink));
  }
  .brand-name {
    font-family: 'Roboto', sans-serif;
    font-weight: 700;
    font-size: 60px;
    color: var(--ink-crimson);
    line-height: 1;
  }
  .brand-tagline {
    font-family: 'Questrial', sans-serif;
    font-size: 15px;
    color: var(--ink-dark);
    margin-top: 6px;
    margin-left: 106px;
    letter-spacing: 0.5px;
  }
  .card-back .brand-lockup { left: 210px; top: 150px; }
  .card-front .brand-lockup { left: 58px; top: 150px; }

  .front-panel {
    position: absolute;
    inset: 0;
    width: 720px;
    height: 411px;
  }
  .company-block {
    position: absolute;
    left: 400px;
    top: 74px;
    width: 290px;
  }
  .company-name {
    font-family: 'Roboto', sans-serif;
    font-weight: 700;
    font-size: 25px;
    color: var(--ink-white);
    white-space: nowrap;
  }
  .company-rule {
    display: flex;
    gap: 24px;
    margin-top: 10px;
    margin-left: 36px;
  }
  .company-rule span {
    width: 76px;
    height: 1.5px;
    background: var(--ink-white);
  }
  .contact-list {
    list-style: none;
    position: absolute;
    left: 440px;
    top: 172px;
    font-family: 'Questrial', sans-serif;
    font-size: 17px;
    color: var(--ink-soft);
    line-height: 1.3;
  }
  .contact-list li {
    display: flex;
    align-items: flex-start;
    gap: 12px;
  }
  .contact-list svg {
    width: 13px;
    height: 13px;
    margin-top: 4px;
    flex: none;
    fill: var(--ink-soft);
  }
</style>
</head>
<body>

  <section class="card card-back" aria-label="Card back">
    <div class="brand-lockup">
      <div class="brand-row">
        <div class="brand-mark"></div>
        <span class="brand-name">Brisk</span>
      </div>
      <span class="brand-tagline">Yoga•Swim•Pole</span>
    </div>
  </section>

  <section class="card card-front" aria-label="Card front">
    <div class="brand-lockup">
      <div class="brand-row">
        <div class="brand-mark"></div>
        <span class="brand-name">Brisk</span>
      </div>
      <span class="brand-tagline">Yoga•Swim•Pole</span>
    </div>

    <svg class="front-panel" viewBox="0 0 720 411" aria-hidden="true">
      <defs>
        <radialGradient id="panelGlow" cx="0.45" cy="0.3" r="0.8">
          <stop offset="0" stop-color="var(--brand-red-light)"/>
          <stop offset="0.6" stop-color="var(--brand-red)"/>
          <stop offset="1" stop-color="var(--brand-red-dark)"/>
        </radialGradient>
      </defs>
      <path d="M318 0 C350 60 345 160 300 196 L306 205 C345 240 352 345 318 411 L720 411 L720 0 Z" fill="var(--accent-orange)"/>
      <path d="M334 0 C366 60 361 160 318 196 L324 205 C361 240 368 345 334 411 L720 411 L720 0 Z" fill="url(#panelGlow)"/>
    </svg>

    <div class="company-block">
      <div class="company-name">Brisk Loom Pte Ltd</div>
      <div class="company-rule"><span></span><span></span></div>
    </div>

    <ul class="contact-list">
      <li>
        <svg viewBox="0 0 24 24"><path d="M6.6 10.8c1.4 2.8 3.8 5.1 6.6 6.6l2.2-2.2c.3-.3.7-.4 1-.2 1.1.4 2.3.6 3.6.6.6 0 1 .4 1 1V20c0 .6-.4 1-1 1C10.6 21 3 13.4 3 4c0-.6.4-1 1-1h3.5c.6 0 1 .4 1 1 0 1.3.2 2.5.6 3.6.1.3 0 .7-.2 1z"/></svg>
        <span>Your Phone Number</span>
      </li>
      <li>
        <svg viewBox="0 0 24 24"><path d="M2 5h20v14H2z M2 5l10 8 10-8" /></svg>
        <span>Your Email address</span>
      </li>
      <li>
        <svg viewBox="0 0 24 24"><path d="M12 2a10 10 0 100 20 10 10 0 000-20zm6.9 6h-3a15 15 0 00-1.3-4A8 8 0 0118.9 8zM12 4c.8 1.2 1.5 2.5 1.9 4h-3.8c.4-1.5 1.1-2.8 1.9-4zM4.3 14a8 8 0 010-4h3.4a16 16 0 000 4zm.8 2h3a15 15 0 001.3 4A8 8 0 015.1 16zm3-8h-3a8 8 0 014.3-4A15 15 0 008.1 8zM12 20c-.8-1.2-1.5-2.5-1.9-4h3.8c-.4 1.5-1.1 2.8-1.9 4zm2.3-6H9.7a14 14 0 010-4h4.6a14 14 0 010 4zm.3 6a15 15 0 001.3-4h3a8 8 0 01-4.3 4zm1.7-6a16 16 0 000-4h3.4a8 8 0 010 4z"/></svg>
        <span>Your website address</span>
      </li>
      <li>
        <svg viewBox="0 0 24 24"><path d="M12 2a7 7 0 00-7 7c0 5.2 7 13 7 13s7-7.8 7-13a7 7 0 00-7-7zm0 9.5a2.5 2.5 0 110-5 2.5 2.5 0 010 5z"/></svg>
        <span>Your Location, City<br>&amp; State</span>
      </li>
    </ul>
  </section>

</body>
</html>
```